Valbrook Data Works

Our company is about IT hardwares and IT solutions. IT hardware such as PC, RAMS, storage and servers. IT solutions such as project management, BA. We are also selling new technology too.

Target Market(s)

Consumer, Small to Medium Business, Corporate

Requirements
Must have
• The business card must have the following:
• Name:
• Title:
• Contact Number:
• Email address:
• Website:
• Color: Must match the logo color upgrade

```html
<!DOCTYPE html>
<html lang="en">
<head>
<meta charset="utf-8">
<title>Valbrook Data Works – Business Card</title>
<link href="https://fonts.googleapis.com/css2?family=Kumbh+Sans:wght@400;700&display=swap" rel="stylesheet">
<style>
  :root {
    --page: #ffffff;
    --card-light: #ffffff;
    --card-dark: #4a4a4a;
    --copper: #c46a2c;
    --ink: #3a3a3a;
    --ink-soft: #4a4a4a;
    --white: #f5f5f5;
  }
  * { margin: 0; padding: 0; box-sizing: border-box; }
  html, body { width: 880px; height: 1200px; overflow: hidden; background: var(--page); }
  body { position: relative; font-family: "Kumbh Sans", sans-serif; color: var(--ink); }

  .card {
    position: absolute;
    left: 161px;
    width: 561px;
    height: 321px;
    border-radius: 28px;
    box-shadow: 0 0 14px rgba(0,0,0,0.28);
  }
  .card--front { top: 222px; background: var(--card-light); }
  .card--back { top: 572px; background: var(--card-dark); }

  .brand {
    position: absolute;
    display: flex;
    flex-direction: column;
    align-items: center;
    text-align: center;
  }
  .brand__mark {
    border: 4px solid var(--copper);
    border-radius: 50%;
  }
  .brand__name {
    font-weight: 700;
    text-transform: uppercase;
    line-height: 1.1;
  }
  .card--front .brand { left: 30px; width: 256px; top: 108px; }
  .card--front .brand__mark { width: 44px; height: 44px; margin-bottom: 14px; }
  .card--front .brand__name { color: var(--ink-soft); font-size: 22px; letter-spacing: 0.5px; }

  .card--back .brand { left: 0; width: 561px; top: 80px; }
  .card--back .brand__mark { width: 68px; height: 68px; margin-bottom: 24px; }
  .card--back .brand__name { color: var(--white); font-size: 34px; letter-spacing: 1px; }

  .divider {
    position: absolute;
    left: 280px;
    top: 98px;
    width: 1px;
    height: 136px;
    background: var(--ink-soft);
  }

  .contact { position: absolute; left: 302px; top: 92px; }
  .contact__name {
    color: var(--copper);
    font-weight: 700;
    font-size: 24px;
    line-height: 1;
  }
  .contact__title { font-size: 13px; margin-top: 7px; }
  .contact__group {
    position: relative;
    padding-left: 46px;
    margin-top: 10px;
    font-size: 13px;
    line-height: 23.5px;
  }
  .contact__group + .contact__group { margin-top: 1px; }
  .contact__icon {
    position: absolute;
    left: 0;
    top: 6px;
    width: 36px;
    height: 36px;
  }
</style>
</head>
<body>

  <section class="card card--front" aria-label="Business card front">
    <div class="brand">
      <span class="brand__mark"></span>
      <span class="brand__name">Valbrook Data Works</span>
    </div>

    <span class="divider"></span>

    <div class="contact">
      <p class="contact__name">NAME:</p>
      <p class="contact__title">Title:</p>

      <div class="contact__group">
        <svg class="contact__icon" viewBox="0 0 36 36" aria-hidden="true">
          <circle cx="18" cy="18" r="16.5" fill="none" stroke="var(--copper)" stroke-width="2"/>
          <path d="M10 15c0-3 4-4 8-4s8 1 8 4v2h-4v-2h-8v2h-4z" fill="var(--ink-soft)"/>
          <path d="M12 18l2-2h8l2 2v7H12z" fill="var(--ink-soft)"/>
          <circle cx="18" cy="21" r="2" fill="#fff"/>
        </svg>
        <p>Cell Phone here</p>
        <p>Telephone here</p>
      </div>

      <div class="contact__group">
        <svg class="contact__icon" viewBox="0 0 36 36" aria-hidden="true">
          <circle cx="18" cy="18" r="16.5" fill="none" stroke="var(--copper)" stroke-width="2"/>
          <g fill="none" stroke="var(--ink-soft)" stroke-width="1.4">
            <circle cx="18" cy="18" r="8"/>
            <ellipse cx="18" cy="18" rx="3.5" ry="8"/>
            <line x1="10" y1="18" x2="26" y2="18"/>
            <line x1="11.5" y1="14" x2="24.5" y2="14"/>
            <line x1="11.5" y1="22" x2="24.5" y2="22"/>
          </g>
        </svg>
        <p>Your email here</p>
        <p>Your website/URL here</p>
      </div>
    </div>
  </section>

  <section class="card card--back" aria-label="Business card back">
    <div class="brand">
      <span class="brand__mark"></span>
      <span class="brand__name">Valbrook Data Works</span>
    </div>
  </section>

</body>
</html>
```